Business card for my company-RMK Design Studio

I do not have a logo-I like red and keeping it clean. Information that should be on the card:
Tom Brakefield AIA
Architecture Planning Interiors
Cell Phone-614.492.5068
email-rmkarchitect1@lunvale.com
www.rmkdesignstudio.net

```html
<!DOCTYPE html>
<html lang="en">
<head>
<meta charset="utf-8">
<title>RMK Design Studio — Business Card</title>
<link rel="stylesheet" href="https://fonts.googleapis.com/css2?family=Montserrat:wght@300;400;700&display=swap">
<style>
  :root {
    --page-bg: #d6d6d6;
    --card-white: #ffffff;
    --brand-red: #e30613;
    --ink-dark: #3a3a3a;
    --ink-light: #8c8c8c;
    --night: #0b0306;
    --photo-red: #c8000c;
  }
  * { box-sizing: border-box; margin: 0; padding: 0; }
  html, body { width: 1200px; height: 846px; overflow: hidden; }
  body {
    background: var(--page-bg);
    display: flex;
    align-items: center;
    justify-content: center;
    gap: 48px;
  }
  .card {
    position: relative;
    width: 532px;
    height: 304px;
    overflow: hidden;
    box-shadow: 0 6px 18px rgba(0,0,0,0.18);
  }

  /* Front face */
  .card-front { background: var(--card-white); }
  .card-front .edge-band {
    position: absolute; left: 0; top: 0; bottom: 0;
    width: 16px; background: var(--brand-red);
  }
  .card-front .content {
    position: absolute; left: 72px; top: 44px; right: 28px;
  }
  .studio-name {
    font-family: "Montserrat", sans-serif;
    font-weight: 400;
    font-size: 28px;
    color: var(--ink-dark);
    letter-spacing: 0.5px;
    line-height: 1;
  }
  .person {
    margin-top: 24px;
    font-family: "Montserrat", sans-serif;
  }
  .person-name {
    font-weight: 700;
    font-size: 19px;
    color: var(--brand-red);
  }
  .person-role {
    margin-top: 3px;
    font-weight: 300;
    font-size: 12px;
    color: var(--ink-light);
  }
  .contact-list {
    list-style: none;
    margin-top: 18px;
    font-family: "Montserrat", sans-serif;
    font-weight: 300;
    font-size: 14px;
    color: var(--ink-light);
  }
  .contact-list li {
    display: flex; align-items: center; gap: 10px;
    height: 22px;
  }
  .contact-list li.address { margin-top: 10px; }
  .contact-list svg {
    width: 16px; height: 16px; flex: none;
    fill: none; stroke: var(--ink-light); stroke-width: 1.1;
  }

  /* Back face */
  .card-back { background: var(--night); }
  .card-back .building-photo {
    position: absolute; inset: 0;
    background:
      linear-gradient(150deg, var(--night) 0%, var(--night) 30%, #5a0208 52%, var(--photo-red) 72%, var(--brand-red) 100%);
  }
  .card-back .studio-name {
    position: absolute; left: 70px; top: 60px;
    font-size: 36px;
    color: var(--brand-red);
  }
</style>
</head>
<body>

  <section class="card card-front" aria-label="Business card front">
    <div class="edge-band"></div>
    <div class="content">
      <h1 class="studio-name">RMK Design Studio</h1>
      <div class="person">
        <p class="person-name">Tom Brakefield AIA</p>
        <p class="person-role">Architecture Planning Interiors</p>
      </div>
      <ul class="contact-list">
        <li>
          <svg viewBox="0 0 16 16"><rect x="4.5" y="1.5" width="7" height="13" rx="1.2"/><line x1="7" y1="12.5" x2="9" y2="12.5"/></svg>
          614.492.5068
        </li>
        <li>
          <svg viewBox="0 0 16 16"><rect x="1.5" y="3.5" width="13" height="9"/><polyline points="1.5,3.5 8,9 14.5,3.5"/></svg>
          rmkarchitect1@lunvale.com
        </li>
        <li>
          <svg viewBox="0 0 16 16"><circle cx="8" cy="8" r="6.5"/><ellipse cx="8" cy="8" rx="3" ry="6.5"/><line x1="1.5" y1="8" x2="14.5" y2="8"/><line x1="2.5" y1="5" x2="13.5" y2="5"/><line x1="2.5" y1="11" x2="13.5" y2="11"/></svg>
          www.rmkdesignstudio.net
        </li>
        <li class="address">
          <svg viewBox="0 0 16 16"><path d="M8 15 C8 15 2.8 9.5 2.8 6.2 A5.2 5.2 0 0 1 13.2 6.2 C13.2 9.5 8 15 8 15 Z"/><circle cx="8" cy="6.2" r="2"/></svg>
          418 Harlow Ave. #112 Columbus, Ohio 43215
        </li>
      </ul>
    </div>
  </section>

  <section class="card card-back" aria-label="Business card back">
    <div class="building-photo" role="img" aria-label="Red-toned photograph of a modern glass-fronted building against a dark sky"></div>
    <h2 class="studio-name">RMK Design Studio</h2>
  </section>

</body>
</html>
```